Copper Ladle, Wine Bar and Bistro

We need a logo and business cards that reflects our wine bar concept. Please refer to the description below.Anthropologist and attorney Maren Holt Pravecky and attorney Dana Rueckl, in consultation with Executive Chef and restauranteur Oren Pask, seek to open Copper Ladle, a wine bar and bistro in the business district of Swarthmore Borough. Our concept, “SAVOURING FAR PLACES BY THE GLASS”, brings together unique, delicious wines from around the world and regional small plates to locals eager to learn about and experience the gustatory joys of lesser known wine-producing locales.Strategically located in downtown Swarthmore, Pennsylvania, near the commuter train, Copper Ladle will be a comfortable, welcoming atmosphere in which to learn about, taste and enjoy interesting wines, dine, meet friends or just have a drink after work. After hours desserts, coffees, teas and other non-alcoholic beverages will be highly attractive to not only town residents but also the nearly 1600 college-aged students who attend Gladwick College.
Target Market(s)
People interested in learning about unusual wine regions. Design must capture small, local, village feel. Think of a family owned vineyard in a small corner of the world that produces great regional wine. Also, design should capture learning, education and taking in new experiences.
Contact Information for Business Card
CopperLadleDenholt.com
Logo Text
Copper Ladle
Colors
Designer to choose colors to be used in the design.
Requirements
Must have
- Small village feel.
Nice to have
- Vines. Grapes. Globe. Try greens and purples.

```html
<!DOCTYPE html>
<html lang="en">
<head>
<meta charset="utf-8">
<title>Copper Ladle – Business Card</title>
<link href="https://fonts.googleapis.com/css2?family=Arvo:wght@400&family=Lato:wght@400&display=swap" rel="stylesheet">
<style>
  :root {
    --backdrop: #2a2a2b;
    --card: #1d1e20;
    --card-back: #1a1b1d;
    --pattern-tone: #232427;
    --wine-red: #c0191f;
    --grey-text: #bdbdbd;
    --rule: #6b6b6b;
    --white: #ffffff;
  }
  * { margin: 0; padding: 0; box-sizing: border-box; }
  html, body { width: 1200px; height: 1108px; overflow: hidden; background: var(--backdrop); }
  .canvas { position: relative; width: 1200px; height: 1108px; }
  .card {
    position: absolute; top: 200px; width: 440px; height: 700px;
    border-radius: 26px; box-shadow: 0 12px 30px rgba(0,0,0,.45); overflow: hidden;
  }
  .card-front { left: 130px; background: var(--card); text-align: center; }
  .card-back { left: 630px; background: var(--card-back); }

  .brand-mark {
    width: 120px; height: 120px; border-radius: 50%;
    background: var(--wine-red); margin: 92px auto 0;
  }
  .brand-name {
    font-family: "Arvo", serif; font-weight: 400; font-size: 52px; color: var(--grey-text);
    margin-top: 44px; white-space: nowrap;
  }
  .person-name {
    font-family: "Arvo", serif; font-weight: 400; font-size: 28px; color: var(--wine-red);
    margin-top: 36px;
  }
  .person-role { font-family: "Lato", sans-serif; font-size: 21px; color: var(--grey-text); margin-top: 2px; }
  .icon-row { display: flex; align-items: center; justify-content: center; gap: 8px; margin: 18px 50px 0; }
  .icon-row .rule { flex: 1; height: 1px; background: var(--rule); }
  .icon-row svg { width: 28px; height: 28px; }
  .contact-list { font-family: "Lato", sans-serif; font-size: 21px; line-height: 30px; color: var(--grey-text); margin-top: 16px; }
  .divider { height: 1px; background: var(--rule); margin: 16px 60px; }
  .address { font-family: "Lato", sans-serif; font-size: 20px; line-height: 28px; color: var(--grey-text); }

  .back-pattern {
    position: absolute; left: 0; top: 0; width: 440px; height: 470px;
    background: linear-gradient(180deg, var(--pattern-tone) 0%, var(--card-back) 100%);
  }
  .back-brand {
    position: absolute; left: 50px; bottom: 128px; white-space: nowrap;
    font-family: "Arvo", serif; font-weight: 400; font-size: 58px; color: var(--white);
  }
  .back-tagline {
    position: absolute; left: 52px; bottom: 92px; white-space: nowrap;
    font-family: "Lato", sans-serif; font-size: 18px; color: var(--white); letter-spacing: .5px;
  }
</style>
</head>
<body>
<main class="canvas">
  <section class="card card-front">
    <div class="brand-mark" aria-hidden="true"></div>
    <h1 class="brand-name">Copper Ladle</h1>
    <p class="person-name">Elias Marrow</p>
    <p class="person-role">Managing Director</p>
    <div class="icon-row">
      <span class="rule"></span>
      <svg viewBox="0 0 28 28" aria-label="Phone"><circle cx="14" cy="14" r="14" fill="var(--wine-red)"/><path d="M9 8c1-1 2-1 3 1l1 2c0 1-1 1-1 2 1 2 2 3 3 4 1 0 1-1 2-1l2 1c2 1 1 2 0 3-3 2-12-6-10-12z" fill="#1d1e20"/></svg>
      <svg viewBox="0 0 28 28" aria-label="Email"><circle cx="14" cy="14" r="14" fill="var(--wine-red)"/><rect x="7" y="9" width="14" height="10" fill="none" stroke="#1d1e20" stroke-width="1.8"/><path d="M7 9l7 6 7-6" fill="none" stroke="#1d1e20" stroke-width="1.8"/></svg>
      <svg viewBox="0 0 28 28" aria-label="Website"><circle cx="14" cy="14" r="14" fill="var(--wine-red)"/><circle cx="14" cy="14" r="7" fill="none" stroke="#1d1e20" stroke-width="1.8"/><path d="M7 14h14M14 7c-3 4-3 10 0 14M14 7c3 4 3 10 0 14" fill="none" stroke="#1d1e20" stroke-width="1.4"/></svg>
      <span class="rule"></span>
    </div>
    <div class="contact-list">
      <p>044-555 018 274</p>
      <p>info@copperladle.com</p>
      <p>www.copperladledenholt.com</p>
    </div>
    <div class="divider"></div>
    <div class="address">
      <p>38, Orchard Row, Denholt,</p>
      <p>19081, Pennsylvania</p>
    </div>
  </section>

  <section class="card card-back">
    <div class="back-pattern" role="img" aria-label="Faint repeating decorative pattern area"></div>
    <h2 class="back-brand">Copper Ladle</h2>
    <p class="back-tagline">SAVOURING FAR PLACES BY THE GLASS</p>
  </section>
</main>
</body>
</html>
```